A Techincal Author needs a site to promote his Programming Books

The StudyAlong series is a collection of books focusing on building the same app with different technologies. The purpose of this project is to design a web site home page that can be used to sell the books.

Expected Deliverables
• StudyAlong Logo as Illustrator file
• Master graphic design files for any relevant web assets
• HTML and CSS for home page, if applicable

Target Market(s)

The target market for our series is web programmers. They are people who have some experience, but want to learn a new tool. Programmers are analytical, logical people who like structure in the things they do.

Here are some things our customers like:

• Chirpline / Postora
• Clan of Ravens / Hollow Marsh / Burning Low
• SmartPhones, Tablets, Stridelets, and other tech gadgets.

The design should try to speak to that market.

Industry/Entity Type

Building

Coding

Coded - Design and coding required

Number of Pages Required

1 page

Requirements
Must have
• The primary tasks for this project are:
• 1) Create "Study Along" Logo.
• * All “NetBrookly” properties use a similar logo approach, with the NetBrookly ball icon on the left, a reflection below it. The company name is on the right, roughly the same size as the ball icon. A tag line underneath the company name, roughly the same size as the reflection.
• * Company Name: Study Along
• * Tagline: Knowledge to Boost Your Career
• * Logo color is up to the discretion of the designer, but should be compatible with the site design.
• * Sample Logos for other NetBrookly properties in Illustrator format are available as attachments to this project.
• 2) Design the Study Along Home Page.
• The home page should follow this format:
• * Logo
• * Nav Bar
• • Buy (The Home Page)
• • About
• • Contact
• * Main Content
• • Home page content detailed in attachment
• * Footer
• • Copyright notice
• • Links to other stuff we do ( net-brook-ly.com | marlontrevick.com | PathPastGrid.com )
Nice to have
• It would be nice to have a book as part of the home page content.
Should not have
• Please do not use the same color scheme as PathPastGrid.com or Gridmora.com or QueryTheGridsmith.com

```html
<!DOCTYPE html>
<html lang="en">
<head>
<meta charset="utf-8">
<title>Study Along – Programming Books</title>
<link href="https://fonts.googleapis.com/css2?family=Roboto:wght@300;400;500;700&display=swap" rel="stylesheet">
<style>
:root{
  --navy:#2f3591;
  --navy-deep:#262a7a;
  --ink:#222;
  --muted:#8a8a8a;
  --rule:#dcdcdc;
  --panel-light:#f2f2f2;
  --panel-mid:#dcdcdc;
  --shadow-block:#221d5c;
  --cover-top:#e6e9ee;
  --cover-band:#3d3585;
  --cover-title:#45397f;
  --mark-red:#c7272d;
  --white:#fff;
}
*{box-sizing:border-box;margin:0;padding:0}
html,body{width:1200px;height:2469px;overflow:hidden;background:var(--white)}
body{position:relative;font-family:'Roboto',sans-serif;color:var(--ink)}

/* Header */
.site-header{position:absolute;left:0;top:0;width:1200px;height:44px;background:var(--white)}
.brand{position:absolute;left:244px;top:10px}
.brand-name{display:block;font-size:22px;font-weight:500;color:var(--navy);letter-spacing:1px;line-height:24px}
.main-nav{position:absolute;left:798px;top:10px;display:flex;align-items:center}
.main-nav a{font-size:10px;color:var(--navy);text-decoration:none;margin-right:15px;line-height:25px}
.main-nav .nav-buy{margin:0 0 0 39px;width:61px;height:25px;background:var(--navy);color:var(--white);font-weight:700;text-align:center;border-radius:2px}

/* Hero */
.hero{position:absolute;left:0;top:44px;width:1200px;height:392px}
.hero-photo{position:absolute;inset:0;background:linear-gradient(90deg,#8a5a43 0%,#3d97c7 14%,#4aa8d8 30%,#c9b3a0 42%,#a35a44 58%,#5f4a66 72%,#b4684f 86%,#7b8aa6 100%)}
.signup-card{position:absolute;left:780px;top:203px;width:201px;height:227px;background:var(--white);border:1px solid #c9c9c9;box-shadow:0 2px 6px rgba(0,0,0,.18);padding:0 13px}
.signup-title{margin-top:10px;font-size:14px;font-weight:500;color:var(--navy)}
.signup-sub{font-size:9px;color:var(--navy);padding-bottom:8px;border-bottom:1px solid #e3e3e3}
.field-label{display:block;font-size:8px;color:var(--muted);margin-top:17px}
.field-input{display:block;width:100%;height:25px;margin-top:4px;background:#f3f3f3;border:1px solid #e2e2e2}
.field-label.second{margin-top:15px}
.signup-submit{display:block;width:100%;height:25px;margin-top:26px;background:linear-gradient(#3a40a3,var(--navy-deep));color:var(--white);border:0;font:700 11px 'Roboto',sans-serif}

/* About */
.about{position:absolute;left:0;top:436px;width:1200px;height:535px}
.author-frame{position:absolute;left:244px;top:101px;width:299px;height:325px}
.author-frame-shadow{position:absolute;left:14px;top:11px;width:285px;height:314px;background:var(--shadow-block)}
.author-photo{position:absolute;left:0;top:0;width:286px;height:314px;background:radial-gradient(ellipse at 55% 60%,#3a3a3a 0%,#6d6d6d 40%,#9a9a9a 75%,#7c7c7c 100%)}
.about-title{position:absolute;left:591px;top:96px;font-size:23px;font-weight:400;color:#3b3b3b}
.about-text{position:absolute;left:591px;top:144px;width:360px;font-size:8.6px;line-height:12.6px;color:var(--muted);font-weight:300}

/* Book sections */
.book-section{position:absolute;left:0;width:1200px;height:499px}
.book-section.light{background:radial-gradient(ellipse at 70% 50%,#fff 0%,var(--panel-light) 55%)}
.book-section.mid{background:var(--panel-mid)}
.section-title{position:absolute;font-size:17px;font-weight:500;color:var(--ink);display:flex;align-items:baseline}
.app-link{margin-left:32px;font-size:9px;font-weight:400;color:#444;text-decoration:underline}
.app-link svg{vertical-align:middle;margin-left:3px}
.offer-list{position:absolute;width:488px;list-style:none}
.offer{position:relative;height:100px;border-bottom:1px solid var(--rule)}
.offer-name{position:absolute;left:0;top:40px;width:155px;display:flex;align-items:center;font-size:11px;color:#555;line-height:13px}
.offer-name svg{flex:none;margin-right:8px}
.offer-price{position:absolute;left:159px;top:44px;font-size:12px;font-weight:700;font-style:italic;color:#333}
.buy{position:absolute;top:35px;width:126px;height:33px;display:flex;align-items:center;justify-content:center;text-decoration:none}
.buy-us{left:223px;background:linear-gradient(#4a4fae,var(--navy-deep));color:var(--white);font-size:12px;font-weight:500;letter-spacing:1px}
.buy-store{left:362px;width:123px;background:var(--white);border:1px solid #ddd;color:#111;font-size:12px;font-weight:700}
.buy-caption{position:absolute;top:75px;width:126px;text-align:center;font-size:7px;color:var(--muted)}
.buy-caption.us{left:223px}
.buy-caption.store{left:362px;width:123px}

/* Book cover */
.book-cover{position:absolute;width:188px;height:277px;background:linear-gradient(160deg,#f1f3f6 0%,var(--cover-top) 50%,#cfd4dc 100%);box-shadow:0 3px 8px rgba(0,0,0,.22);text-align:center}
.book-cover::before{content:"";position:absolute;left:0;top:0;width:7px;height:100%;background:linear-gradient(90deg,#9aa0aa,#d6dae0)}
.cover-series{margin-top:15px;font-size:27px;font-weight:500;color:var(--cover-title)}
.cover-mark{display:block;width:38px;height:38px;margin:14px auto 0;background:var(--mark-red)}
.cover-title{margin-top:12px;font-size:13px;font-weight:700;line-height:17px;color:#222}
.cover-band{position:absolute;left:0;bottom:0;width:100%;height:44px;background:var(--cover-band);color:var(--white);font-size:11px;font-weight:500;letter-spacing:1px;line-height:44px}
</style>
</head>
<body>

<header class="site-header">
  <div class="brand">
    <span class="brand-name">STUDY ALONG</span>
  </div>
  <nav class="main-nav">
    <a href="#about">About</a>
    <a href="#contact">Contact</a>
    <a href="#buy" class="nav-buy">BUY</a>
  </nav>
</header>

<section class="hero">
  <div class="hero-photo" role="img" aria-label="Photo of a student reading in front of library bookshelves"></div>
  <form class="signup-card">
    <h2 class="signup-title">Sign Up</h2>
    <p class="signup-sub">for a free sample</p>
    <label class="field-label">Your Name</label>
    <span class="field-input"></span>
    <label class="field-label second">Your Email</label>
    <span class="field-input"></span>
    <button class="signup-submit" type="button">Submit</button>
  </form>
</section>

<section class="about" id="about">
  <div class="author-frame">
    <div class="author-frame-shadow"></div>
    <div class="author-photo" role="img" aria-label="Black and white portrait of the author"></div>
  </div>
  <h2 class="about-title">About Us</h2>
  <p class="about-text">Marlon Trevick has spent twenty years building software for teams of every size, and he writes the way he codes: one small step at a time. Each Study Along book builds the same task tracker app with a different stack, so you can compare tools side by side and learn what really changes. Start with the free sample, follow the code, and ship a working app by the final chapter. Clear examples, honest explanations and no filler along the way.</p>
</section>

<section class="book-section light" style="top:971px">
  <h2 class="section-title" style="left:244px;top:40px">Vectorly 1.5 &amp; Stilt <a class="app-link" href="#">View App Link<svg width="9" height="9" viewBox="0 0 10 10"><path d="M4 6 6 4M3 5 1.8 6.2a1.6 1.6 0 0 0 2.2 2.2L5.2 7M7 5l1.2-1.2A1.6 1.6 0 0 0 6 1.6L4.8 2.8" fill="none" stroke="#444" stroke-width="1"/></svg></a></h2>
  <ul class="offer-list" style="left:244px;top:64px">
    <li class="offer"><span class="offer-name"><svg width="16" height="18" viewBox="0 0 16 18"><rect x="1" y="1" width="14" height="16" fill="#eee" stroke="#999"/><line x1="4" y1="1" x2="4" y2="17" stroke="#999"/></svg>With Mock Services</span><span class="offer-price">$5.99</span><a class="buy buy-us" href="#">STUDY ALONG</a><a class="buy buy-store" href="#">Shelfmart</a><span class="buy-caption us">Buy from Us</span><span class="buy-caption store">Buy from Shelfmart</span></li>
    <li class="offer"><span class="offer-name"><svg width="16" height="18" viewBox="0 0 16 18"><rect x="1" y="1" width="14" height="16" fill="#eee" stroke="#999"/><line x1="4" y1="1" x2="4" y2="17" stroke="#999"/></svg>With NodeRun Services</span><span class="offer-price">$5.99</span><a class="buy buy-us" href="#">STUDY ALONG</a><a class="buy buy-store" href="#">Shelfmart</a><span class="buy-caption us">Buy from Us</span><span class="buy-caption store">Buy from Shelfmart</span></li>
    <li class="offer"><span class="offer-name"><svg width="16" height="18" viewBox="0 0 16 18"><rect x="1" y="1" width="14" height="16" fill="#eee" stroke="#999"/><line x1="4" y1="1" x2="4" y2="17" stroke="#999"/></svg>With ColdForge<br>Services</span><span class="offer-price">$5.99</span><a class="buy buy-us" href="#">STUDY ALONG</a><a class="buy buy-store" href="#">Shelfmart</a><span class="buy-caption us">Buy from Us</span><span class="buy-caption store">Buy from Shelfmart</span></li>
    <li class="offer"><span class="offer-name"><svg width="16" height="18" viewBox="0 0 16 18"><rect x="1" y="1" width="14" height="16" fill="#eee" stroke="#999"/><line x1="4" y1="1" x2="4" y2="17" stroke="#999"/></svg>Buy Them All</span><span class="offer-price">$9.99</span><a class="buy buy-us" href="#">STUDY ALONG</a><a class="buy buy-store" href="#">Shelfmart</a><span class="buy-caption us">Buy from Us</span><span class="buy-caption store">Buy from Shelfmart</span></li>
  </ul>
  <div class="book-cover" style="left:754px;top:135px">
    <p class="cover-series">Stilt</p>
    <span class="cover-mark"></span>
    <p class="cover-title">Vectorly 1.5 &amp;<br>Stilt</p>
    <div class="cover-band">STUDY ALONG</div>
  </div>
</section>

<section class="book-section mid" style="top:1470px">
  <h2 class="section-title" style="left:489px;top:39px">Vectorly 1.5 &amp; Stilt <a class="app-link" href="#">View App Link<svg width="9" height="9" viewBox="0 0 10 10"><path d="M4 6 6 4M3 5 1.8 6.2a1.6 1.6 0 0 0 2.2 2.2L5.2 7M7 5l1.2-1.2A1.6 1.6 0 0 0 6 1.6L4.8 2.8" fill="none" stroke="#444" stroke-width="1"/></svg></a></h2>
  <ul class="offer-list" style="left:489px;top:62px">
    <li class="offer"><span class="offer-name"><svg width="16" height="18" viewBox="0 0 16 18"><rect x="1" y="1" width="14" height="16" fill="#eee" stroke="#999"/><line x1="4" y1="1" x2="4" y2="17" stroke="#999"/></svg>With Mock Services</span><span class="offer-price">$5.99</span><a class="buy buy-us" href="#">STUDY ALONG</a><a class="buy buy-store" href="#">Shelfmart</a><span class="buy-caption us">Buy from Us</span><span class="buy-caption store">Buy from Shelfmart</span></li>
    <li class="offer"><span class="offer-name"><svg width="16" height="18" viewBox="0 0 16 18"><rect x="1" y="1" width="14" height="16" fill="#eee" stroke="#999"/><line x1="4" y1="1" x2="4" y2="17" stroke="#999"/></svg>With NodeRun Services</span><span class="offer-price">$5.99</span><a class="buy buy-us" href="#">STUDY ALONG</a><a class="buy buy-store" href="#">Shelfmart</a><span class="buy-caption us">Buy from Us</span><span class="buy-caption store">Buy from Shelfmart</span></li>
    <li class="offer"><span class="offer-name"><svg width="16" height="18" viewBox="0 0 16 18"><rect x="1" y="1" width="14" height="16" fill="#eee" stroke="#999"/><line x1="4" y1="1" x2="4" y2="17" stroke="#999"/></svg>With ColdForge<br>Services</span><span class="offer-price">$5.99</span><a class="buy buy-us" href="#">STUDY ALONG</a><a class="buy buy-store" href="#">Shelfmart</a><span class="buy-caption us">Buy from Us</span><span class="buy-caption store">Buy from Shelfmart</span></li>
    <li class="offer"><span class="offer-name"><svg width="16" height="18" viewBox="0 0 16 18"><rect x="1" y="1" width="14" height="16" fill="#eee" stroke="#999"/><line x1="4" y1="1" x2="4" y2="17" stroke="#999"/></svg>Buy Them All</span><span class="offer-price">$9.99</span><a class="buy buy-us" href="#">STUDY ALONG</a><a class="buy buy-store" href="#">Shelfmart</a><span class="buy-caption us">Buy from Us</span><span class="buy-caption store">Buy from Shelfmart</span></li>
  </ul>
  <div class="book-cover" style="left:260px;top:133px">
    <p class="cover-series">Stilt</p>
    <span class="cover-mark"></span>
    <p class="cover-title">Vectorly 1.5 &amp;<br>Stilt</p>
    <div class="cover-band">STUDY ALONG</div>
  </div>
</section>

<section class="book-section light" style="top:1969px;height:500px">
  <h2 class="section-title" style="left:244px;top:40px">Vectorly 1.5 &amp; Stilt <a class="app-link" href="#">View App Link<svg width="9" height="9" viewBox="0 0 10 10"><path d="M4 6 6 4M3 5 1.8 6.2a1.6 1.6 0 0 0 2.2 2.2L5.2 7M7 5l1.2-1.2A1.6 1.6 0 0 0 6 1.6L4.8 2.8" fill="none" stroke="#444" stroke-width="1"/></svg></a></h2>
  <ul class="offer-list" style="left:244px;top:64px">
    <li class="offer"><span class="offer-name"><svg width="16" height="18" viewBox="0 0 16 18"><rect x="1" y="1" width="14" height="16" fill="#eee" stroke="#999"/><line x1="4" y1="1" x2="4" y2="17" stroke="#999"/></svg>With Mock Services</span><span class="offer-price">$5.99</span><a class="buy buy-us" href="#">STUDY ALONG</a><a class="buy buy-store" href="#">Shelfmart</a><span class="buy-caption us">Buy from Us</span><span class="buy-caption store">Buy from Shelfmart</span></li>
    <li class="offer"><span class="offer-name"><svg width="16" height="18" viewBox="0 0 16 18"><rect x="1" y="1" width="14" height="16" fill="#eee" stroke="#999"/><line x1="4" y1="1" x2="4" y2="17" stroke="#999"/></svg>With NodeRun Services</span><span class="offer-price">$5.99</span><a class="buy buy-us" href="#">STUDY ALONG</a><a class="buy buy-store" href="#">Shelfmart</a><span class="buy-caption us">Buy from Us</span><span class="buy-caption store">Buy from Shelfmart</span></li>
    <li class="offer"><span class="offer-name"><svg width="16" height="18" viewBox="0 0 16 18"><rect x="1" y="1" width="14" height="16" fill="#eee" stroke="#999"/><line x1="4" y1="1" x2="4" y2="17" stroke="#999"/></svg>With ColdForge<br>Services</span><span class="offer-price">$5.99</span><a class="buy buy-us" href="#">STUDY ALONG</a><a class="buy buy-store" href="#">Shelfmart</a><span class="buy-caption us">Buy from Us</span><span class="buy-caption store">Buy from Shelfmart</span></li>
    <li class="offer"><span class="offer-name"><svg width="16" height="18" viewBox="0 0 16 18"><rect x="1" y="1" width="14" height="16" fill="#eee" stroke="#999"/><line x1="4" y1="1" x2="4" y2="17" stroke="#999"/></svg>Buy Them All</span><span class="offer-price">$9.99</span><a class="buy buy-us" href="#">STUDY ALONG</a><a class="buy buy-store" href="#">Shelfmart</a><span class="buy-caption us">Buy from Us</span><span class="buy-caption store">Buy from Shelfmart</span></li>
  </ul>
  <div class="book-cover" style="left:754px;top:135px">
    <p class="cover-series">Stilt</p>
    <span class="cover-mark"></span>
    <p class="cover-title">Vectorly 1.5 &amp;<br>Stilt</p>
    <div class="cover-band">STUDY ALONG</div>
  </div>
</section>

</body>
</html>
```